School Website

I need a design for a School (2 sections: Primary 6-12 years and Secondary 12-18 years). The first page is just a choice of the 2 sections. After we'll need 2 websites (with the same structure: Menu, ...) but with different colors. In fact, we need for end of October, 6 design of school website. So the best websites are going to be made available to you in the future (in pixelharbr) but privately.

Target Market(s)

Public, Parents, ...

Coding

Coded - Design and coding required

Number of Pages Required

5+ page

Font styles to use
Sans Serif

Colors
34a6d7
85cae6
cee9f5
ffffff

Requirements
Must have
• You can check the old Website: http: / /velmok.be We need the same pages with the same content. Menu: - HomePage - News and communication (like blog page) - Activities (like blog page, with photo gallery) - Contact (Contact form + maps) - In the main menu, we need a special button to connect to an external Website ( button needs to be different than the other menu items The name of this button is "Parents Area"). The logo of 2 sections are attached. Please use it for the design and the choice of colors.
Nice to have
• This is a web design of other school that we like: https://www.quintel.be

```html
<!DOCTYPE html>
<html lang="en">
<head>
<meta charset="utf-8">
<title>Lycée Royal de Velmont — Secondary School</title>
<link href="https://fonts.googleapis.com/css2?family=Fira+Sans:ital,wght@0,400;0,500;0,600;0,700;1,400&display=swap" rel="stylesheet">
<style>
:root{
  --green:#7dbb2c;
  --green-dark:#3f7d18;
  --ink:#2b2b2b;
  --muted:#6d6d6d;
  --blue:#2f8fcf;
  --sky:#27a3d8;
  --panel:#f0f0f0;
  --night:#161a24;
  --white:#ffffff;
  --sea:#a9d3ef;
  --land:#f1ead0;
  --pin:#e8453c;
}
*{box-sizing:border-box;margin:0;padding:0}
html,body{width:1200px;height:4392px;overflow:hidden}
body{position:relative;background:var(--white);font-family:"Fira Sans",sans-serif;color:var(--ink)}
.abs{position:absolute}
.topbar{left:0;top:0;width:1200px;height:41px;background:var(--green);color:#fff;font-size:15px;font-weight:600}
.topbar .item{position:absolute;top:11px;display:flex;align-items:center;gap:7px}
.topbar .social{position:absolute;top:10px;right:50px;display:flex;gap:8px}
.topbar .social span{width:21px;height:21px;border:2px solid #fff;border-radius:50%}
.header{left:0;top:41px;width:1200px;height:90px;background:#fff}
.brand{position:absolute;left:52px;top:22px;display:flex;align-items:center;gap:10px;font-size:24px;font-weight:700;color:var(--blue)}
.brand .dot{width:44px;height:44px;border-radius:50%;background:var(--blue)}
.nav{position:absolute;left:494px;top:34px;display:flex;gap:36px;font-size:15px;font-weight:600}
.parents{position:absolute;left:1009px;top:27px;width:145px;height:38px;border-radius:19px;background:var(--green-dark);color:#fff;font-size:16px;font-weight:600;display:flex;align-items:center;justify-content:center;box-shadow:0 3px 0 var(--green)}
.hero{left:0;top:131px;width:1200px;height:470px;overflow:hidden}
.hero .photo{position:absolute;inset:0;background:linear-gradient(100deg,#5e3a2e 0%,#9a5f52 22%,#c58d74 45%,#d4a98c 62%,#9a6a55 82%,#5a3a30 100%)}
.hero .photo::after{content:"";position:absolute;inset:0;background:rgba(0,0,0,.18)}
.hero h1{position:absolute;top:58px;width:1200px;text-align:center;color:#fff;font-weight:500;line-height:1.15;text-shadow:0 2px 6px rgba(0,0,0,.4)}
.hero h1 .l1{display:block;font-size:58px}
.hero h1 .l2{display:block;font-size:60px}
.hero h1 .l3{display:block;font-size:40px}
.btn-dark{position:absolute;left:508px;top:299px;width:184px;height:50px;border-radius:25px;background:#111;color:#fff;font-size:19px;font-weight:500;display:flex;align-items:center;justify-content:center;gap:8px}
.dots{display:flex;gap:26px;align-items:center;justify-content:center;width:1200px}
.dots i{width:11px;height:11px;border-radius:50%;background:var(--green);display:block}
.dots i.on{width:20px;height:20px;border:3px solid var(--green);background-clip:content-box;background-color:var(--green);padding:2px}
.hero .dots i{background:#fff}
.hero .dots i.on{background:var(--green);background-clip:content-box}
.card{background:#fff;box-shadow:0 0 10px rgba(0,0,0,.15);text-align:center}
.feature{top:648px;width:510px;height:261px}
.feature h3{position:absolute;top:148px;width:100%;font-size:19px;font-weight:600;color:var(--green)}
.pill{display:inline-flex;align-items:center;gap:7px;height:38px;padding:0 22px;border-radius:19px;background:#fff;box-shadow:0 2px 7px rgba(0,0,0,.25);font-size:14px;font-weight:500;color:var(--ink)}
.feature .pill{position:absolute;top:192px;left:50%;transform:translateX(-50%)}
.moreinfo{left:49px;top:965px;width:1101px;height:105px;background:linear-gradient(90deg,#23401a,#4c7a2b 50%,#6a9a3a 78%,#b08a5a 90%,#8fae6a);}
.moreinfo h2{position:absolute;left:23px;top:36px;color:#fff;font-size:30px;font-weight:600}
.moreinfo .call{position:absolute;right:52px;top:26px;height:52px;width:175px;border-radius:26px;background:#fff;font-size:20px;font-weight:600;display:flex;align-items:center;justify-content:center;gap:10px}
.news{left:0;top:1125px;width:1200px;height:668px;background:var(--panel)}
.section-title{font-size:29px;font-weight:600;color:var(--ink)}
.arrows{position:absolute;right:56px;top:54px;display:flex;gap:10px}
.arrows span{width:32px;height:24px;background:#111;display:flex;align-items:center;justify-content:center}
.post{position:absolute;top:124px;width:339px}
.post .img{height:246px}
.post h4{margin-top:31px;font-size:19px;font-weight:600;color:var(--green)}
.post .meta{margin-top:14px;padding:10px 0;border-top:1px solid #ddd;display:flex;justify-content:space-between;font-size:12px;font-weight:600;color:#555;text-transform:uppercase}
.post .meta span{display:flex;align-items:center;gap:8px}
.post p{margin-top:8px;font-size:12.5px;line-height:21px;color:#555}
.post .pill{margin-top:16px;margin-left:-6px}
.team{left:48px;top:1846px;width:1102px;height:545px}
.team h2{position:absolute;top:45px;width:100%}
.member{position:absolute;top:131px;width:240px;text-align:center}
.member .face{width:170px;height:170px;margin:0 auto;border-radius:50%;background:radial-gradient(circle at 50% 62%,#d9a585 0%,#c89478 22%,#8a6a55 36%,#d8d8d8 52%,#e8e8e8 100%);box-shadow:-6px 6px 0 #111,2px 8px 0 var(--green)}
.member h4{margin-top:30px;font-size:19px;font-weight:600;color:var(--green)}
.member em{display:block;margin-top:10px;font-size:14px;color:#777}
.member b{display:block;margin-top:10px;font-size:14px;font-weight:500;color:#555}
.contacts{left:49px;top:2443px;width:340px;height:497px;text-align:left}
.contacts h2{position:absolute;left:39px;top:45px;font-size:29px}
.contacts .inner{position:absolute;left:40px;top:106px;width:262px;height:364px;background:#fff;box-shadow:0 0 8px rgba(0,0,0,.15);padding:18px 22px}
.person{padding:6px 0 12px;border-bottom:1px solid #ddd;margin-bottom:16px}
.person h5{font-size:15px;font-weight:600;color:var(--blue)}
.person em{display:block;margin-top:8px;font-size:14px;color:#777}
.person .tel{margin-top:10px;display:flex;gap:12px;align-items:center;font-size:14px;color:#555}
.activities-title{left:440px;top:2435px}
.activities{left:441px;top:2516px;width:699px;height:428px}
.event{position:absolute;left:57px;width:586px;height:160px;background:#fff;box-shadow:0 0 8px rgba(0,0,0,.15);text-align:left}
.event .img{position:absolute;left:0;top:0;width:242px;height:160px}
.event .date{position:absolute;left:0;top:0;width:58px;height:98px;background:#111;color:#fff;font-weight:600;text-align:center;padding-top:14px}
.event .date small{display:block;font-size:18px}
.event .date span{display:block;font-size:24px;margin-top:8px}
.event h4{position:absolute;left:262px;top:22px;font-size:19px;font-weight:500}
.event .row{position:absolute;left:262px;display:flex;gap:16px;align-items:center;font-size:13px;color:#555}
.gallery{left:0;top:2991px;width:1200px;height:660px;overflow:hidden}
.gallery h2{position:absolute;top:40px;width:100%;text-align:center;color:#fff;font-size:29px;font-weight:600}
.shot{position:absolute;width:251px;height:195px;border:3px solid #fff}
.contact{left:0;top:3760px;width:1200px;height:480px;overflow:hidden}
.map{left:72px;top:70px;width:528px;height:406px;clip-path:polygon(0 28%,100% 0,100% 100%,0 100%);
  background:
    radial-gradient(ellipse 120px 90px at 60% 58%,#f6e7a8 0%,transparent 70%),
    radial-gradient(ellipse 260px 200px at 75% 70%,#efe3b8 0%,transparent 75%),
    linear-gradient(135deg,var(--sea) 0%,var(--sea) 24%,#cfe4ec 30%,var(--land) 40%,#f3ecc8 70%,#e6dfbf 100%)}
.map-pin{left:395px;top:176px}
.field{position:absolute;background:#fff;border-radius:6px;font-size:14px;font-style:italic;color:#777;padding:12px 18px}
.submit{position:absolute;left:796px;top:396px;width:159px;height:53px;border-radius:27px;background:var(--sky);color:#fff;font-size:20px;font-weight:600;display:flex;align-items:center;justify-content:center;gap:8px}
.footer{left:0;top:4312px;width:1200px;height:80px;background:#0f1624}
.footer p{position:absolute;left:50px;top:34px;color:#9aa3b5;font-size:14px}
.footer .social{position:absolute;left:934px;top:19px;display:flex;gap:16px}
.footer .social span{width:42px;height:42px;border:3px solid #fff;border-radius:50%}
</style>
</head>
<body>

<div class="abs topbar">
  <div class="item" style="left:50px"><svg width="14" height="14" viewBox="0 0 24 24"><path fill="#fff" d="M6.6 10.8a15 15 0 0 0 6.6 6.6l2.2-2.2c.3-.3.7-.4 1-.2 1.1.4 2.3.6 3.6.6.6 0 1 .4 1 1V20c0 .6-.4 1-1 1A17 17 0 0 1 3 4c0-.6.4-1 1-1h3.5c.6 0 1 .4 1 1 0 1.3.2 2.5.6 3.6.1.3 0 .7-.2 1z"/></svg>+32 81 47 60 13</div>
  <div class="item" style="left:198px"><svg width="14" height="18" viewBox="0 0 24 30"><path fill="#fff" d="M12 0a10 10 0 0 0-10 10c0 8 10 20 10 20s10-12 10-20A10 10 0 0 0 12 0zm0 14a4 4 0 1 1 0-8 4 4 0 0 1 0 8z"/></svg>Rue des Tilleuls , Belgium</div>
  <div class="item" style="left:416px"><svg width="16" height="16" viewBox="0 0 24 24"><circle cx="12" cy="12" r="10" fill="none" stroke="#fff" stroke-width="2.4"/><path d="M12 6v6h5" stroke="#fff" stroke-width="2.4" fill="none"/></svg>Mon- Fri 7 am - 6 pm</div>
  <div class="social"><span></span><span></span><span></span></div>
</div>

<div class="abs header">
  <div class="brand"><span class="dot"></span>Lycée Royal de Velmont</div>
  <nav class="nav"><span>Home</span><span>News</span><span>Activities</span><span>Gallery</span><span>Contact</span></nav>
  <div class="parents">Parents Area</div>
</div>

<section class="abs hero">
  <div class="photo" role="img" aria-label="Group of smiling secondary school students"></div>
  <h1><span class="l1">WELCOME TO</span><span class="l2">Lycée Royal de Velmont</span><span class="l3">Secondary School</span></h1>
  <div class="btn-dark"><svg width="16" height="16" viewBox="0 0 24 24"><path fill="#fff" d="M6.6 10.8a15 15 0 0 0 6.6 6.6l2.2-2.2c.3-.3.7-.4 1-.2 1.1.4 2.3.6 3.6.6.6 0 1 .4 1 1V20c0 .6-.4 1-1 1A17 17 0 0 1 3 4c0-.6.4-1 1-1h3.5c.6 0 1 .4 1 1 0 1.3.2 2.5.6 3.6.1.3 0 .7-.2 1z"/></svg>Call Us</div>
  <svg class="abs" style="left:0;top:0" width="1200" height="470" viewBox="0 0 1200 470">
    <path d="M0 330 Q600 520 1200 320 L1200 470 L0 470 Z" fill="#fff"/>
    <path d="M0 330 Q420 480 1200 320 L1200 345 Q560 530 0 336 Z" fill="var(--green)"/>
  </svg>
  <div class="abs dots" style="top:397px;left:0"><i class="on"></i><i></i><i></i><i></i></div>
</section>

<div class="abs card feature" style="left:66px">
  <svg class="abs" style="left:205px;top:26px" width="100" height="100" viewBox="0 0 100 100"><circle cx="50" cy="50" r="44" fill="none" stroke="var(--green)" stroke-width="9"/><path d="M30 20 A35 35 0 1 0 50 15" fill="none" stroke="#111" stroke-width="7"/><path d="M50 28v24h20" fill="none" stroke="#111" stroke-width="7"/></svg>
  <h3>OUR SCHEDULES AND DAYCARE</h3>
  <span class="pill">Know More <svg width="16" height="10" viewBox="0 0 16 10"><path d="M0 5h14M10 1l4 4-4 4" stroke="var(--blue)" stroke-width="2" fill="none"/></svg></span>
</div>
<div class="abs card feature" style="left:619px">
  <svg class="abs" style="left:210px;top:28px" width="90" height="92" viewBox="0 0 90 92"><path d="M20 28 Q40 -2 70 12 Q58 18 55 30 Q40 22 20 28Z" fill="var(--green)"/><path d="M46 22 L58 84" stroke="#111" stroke-width="4"/><path d="M10 60 L40 80 M14 80 L40 62" stroke="#111" stroke-width="4"/></svg>
  <h3>SCHOOL HOLIDAYS</h3>
  <span class="pill">Know More <svg width="16" height="10" viewBox="0 0 16 10"><path d="M0 5h14M10 1l4 4-4 4" stroke="var(--blue)" stroke-width="2" fill="none"/></svg></span>
</div>

<div class="abs moreinfo" role="img" aria-label="Grass field with stacked books">
  <h2>More Information</h2>
  <div class="call"><svg width="24" height="24" viewBox="0 0 24 24"><path fill="var(--blue)" d="M6.6 10.8a15 15 0 0 0 6.6 6.6l2.2-2.2c.3-.3.7-.4 1-.2 1.1.4 2.3.6 3.6.6.6 0 1 .4 1 1V20c0 .6-.4 1-1 1A17 17 0 0 1 3 4c0-.6.4-1 1-1h3.5c.6 0 1 .4 1 1 0 1.3.2 2.5.6 3.6.1.3 0 .7-.2 1z"/></svg>Call Us</div>
</div>

<section class="abs news">
  <h2 class="section-title abs" style="left:48px;top:48px">LATEST NEWS</h2>
  <div class="arrows"><span><svg width="8" height="12"><path d="M7 1 2 6l5 5" stroke="#fff" stroke-width="2" fill="none"/></svg></span><span><svg width="8" height="12"><path d="M1 1l5 5-5 5" stroke="#fff" stroke-width="2" fill="none"/></svg></span></div>

  <article class="post" style="left:48px">
    <div class="img" role="img" aria-label="Cheerful students in front of a school" style="background:linear-gradient(#7fc4e8,#e2c35a 45%,#7a5a45)"></div>
    <h4>Loreum Ipsum Dummy Text</h4>
    <div class="meta"><span>▦ Auguest 23,2019</span><span>No Comments</span></div>
    <p>Great progress is developing at the Conco B Loreum tex ! More documentation will come as this project pulls together.</p>
    <span class="pill">Know More <svg width="16" height="10" viewBox="0 0 16 10"><path d="M0 5h14M10 1l4 4-4 4" stroke="var(--blue)" stroke-width="2" fill="none"/></svg></span>
  </article>
  <article class="post" style="left:424px">
    <div class="img" role="img" aria-label="Schoolgirl in front of a chalkboard" style="background:linear-gradient(90deg,#2f6b3a,#e3a88a 50%,#e06ca8)"></div>
    <h4>Loreum Ipsum Dummy Text</h4>
    <div class="meta"><span>▦ Auguest 23,2019</span><span>No Comments</span></div>
    <p>Great progress is developing at the Conco B Loreum tex ! More documentation will come as this project pulls together.</p>
    <span class="pill">Know More <svg width="16" height="10" viewBox="0 0 16 10"><path d="M0 5h14M10 1l4 4-4 4" stroke="var(--blue)" stroke-width="2" fill="none"/></svg></span>
  </article>
  <article class="post" style="left:801px">
    <div class="img" role="img" aria-label="Two students holding books" style="background:linear-gradient(90deg,#f4f4f4,#8a5e48 35%,#3a4a6a 70%,#f4f4f4)"></div>
    <h4>Loreum Ipsum Dummy Text</h4>
    <div class="meta"><span>▦ Auguest 23,2019</span><span>No Comments</span></div>
    <p>Great progress is developing at the Conco B Loreum tex ! More documentation will come as this project pulls together.</p>
    <span class="pill">Know More <svg width="16" height="10" viewBox="0 0 16 10"><path d="M0 5h14M10 1l4 4-4 4" stroke="var(--blue)" stroke-width="2" fill="none"/></svg></span>
  </article>
</section>

<section class="abs card team">
  <h2 class="section-title">OUR TEACHING TEAM</h2>
  <div class="member" style="left:33px"><div class="face" role="img" aria-label="Portrait photo of teacher Maren Colson"></div><h4>MAREN COLSON</h4><em>Kindergarten section</em><b>Holder of the class of M1</b></div>
  <div class="member" style="left:302px"><div class="face" role="img" aria-label="Portrait photo of teacher Maren Colson"></div><h4>MAREN COLSON</h4><em>Kindergarten section</em><b>Holder of the class of M1</b></div>
  <div class="member" style="left:572px"><div class="face" role="img" aria-label="Portrait photo of teacher Maren Colson"></div><h4>MAREN COLSON</h4><em>Kindergarten section</em><b>Holder of the class of M1</b></div>
  <div class="member" style="left:841px"><div class="face" role="img" aria-label="Portrait photo of teacher Maren Colson"></div><h4>MAREN COLSON</h4><em>Kindergarten section</em><b>Holder of the class of M1</b></div>
  <div class="abs dots" style="left:-48px;top:472px"><i class="on"></i><i></i><i></i><i></i></div>
</section>

<section class="abs card contacts">
  <h2 class="section-title">USEFUL CONTACTS</h2>
  <div class="inner">
    <div class="person"><h5>MRS ODILE RAMAUX</h5><em>Prefect of studies</em><div class="tel"><svg width="22" height="22" viewBox="0 0 24 24"><path fill="var(--blue)" d="M6.6 10.8a15 15 0 0 0 6.6 6.6l2.2-2.2c.3-.3.7-.4 1-.2 1.1.4 2.3.6 3.6.6.6 0 1 .4 1 1V20c0 .6-.4 1-1 1A17 17 0 0 1 3 4c0-.6.4-1 1-1h3.5c.6 0 1 .4 1 1 0 1.3.2 2.5.6 3.6.1.3 0 .7-.2 1z"/></svg>081 -00-0057</div></div>
    <div class="person"><h5>MRS LISE VANBREL</h5><em>Secretariat</em><div class="tel"><svg width="22" height="22" viewBox="0 0 24 24"><path fill="var(--blue)" d="M6.6 10.8a15 15 0 0 0 6.6 6.6l2.2-2.2c.3-.3.7-.4 1-.2 1.1.4 2.3.6 3.6.6.6 0 1 .4 1 1V20c0 .6-.4 1-1 1A17 17 0 0 1 3 4c0-.6.4-1 1-1h3.5c.6 0 1 .4 1 1 0 1.3.2 2.5.6 3.6.1.3 0 .7-.2 1z"/></svg>081 -00-0057</div></div>
    <div style="text-align:center;margin-top:22px"><span class="pill">View All <svg width="16" height="10" viewBox="0 0 16 10"><path d="M0 5h14M10 1l4 4-4 4" stroke="var(--blue)" stroke-width="2" fill="none"/></svg></span></div>
  </div>
</section>

<h2 class="abs section-title activities-title">ACTIVITIES</h2>
<section class="abs card activities">
  <div class="event" style="top:29px">
    <div class="img" role="img" aria-label="School sports hall" style="background:linear-gradient(#c98a4a,#e8e2d8 50%,#9a8a7a)"></div>
    <div class="date"><small>SEPT</small><span>20</span></div>
    <h4>Loreum ipsum dummy text</h4>
    <div class="row" style="top:70px"><svg width="22" height="22" viewBox="0 0 24 24"><circle cx="12" cy="12" r="10" fill="none" stroke="var(--blue)" stroke-width="2"/><path d="M12 6v6h5" stroke="var(--blue)" stroke-width="2" fill="none"/></svg>12:00 p.m - 5:00 p.m</div>
    <div class="row" style="top:112px"><svg width="20" height="26" viewBox="0 0 24 30"><path fill="var(--sky)" d="M12 0a10 10 0 0 0-10 10c0 8 10 20 10 20s10-12 10-20A10 10 0 0 0 12 0zm0 14a4 4 0 1 1 0-8 4 4 0 0 1 0 8z"/></svg>Loreum ipsum dummy text ,14th Etd.</div>
  </div>
  <div class="event" style="top:206px">
    <div class="img" role="img" aria-label="Students in protective suits on an outing" style="background:linear-gradient(#6e7a6a,#dfe3ea 50%,#4a5560)"></div>
    <div class="date"><small>SEPT</small><span>20</span></div>
    <h4>Loreum ipsum dummy text</h4>
    <div class="row" style="top:70px"><svg width="22" height="22" viewBox="0 0 24 24"><circle cx="12" cy="12" r="10" fill="none" stroke="var(--blue)" stroke-width="2"/><path d="M12 6v6h5" stroke="var(--blue)" stroke-width="2" fill="none"/></svg>12:00 p.m - 5:00 p.m</div>
    <div class="row" style="top:112px"><svg width="20" height="26" viewBox="0 0 24 30"><path fill="var(--sky)" d="M12 0a10 10 0 0 0-10 10c0 8 10 20 10 20s10-12 10-20A10 10 0 0 0 12 0zm0 14a4 4 0 1 1 0-8 4 4 0 0 1 0 8z"/></svg>Loreum ipsum dummy text ,14th Etd.</div>
  </div>
  <div class="abs dots" style="left:-441px;top:391px"><i class="on"></i><i></i><i></i><i></i></div>
</section>

<section class="abs gallery">
  <svg class="abs" style="left:0;top:0" width="1200" height="660" viewBox="0 0 1200 660">
    <defs><linearGradient id="night" x1="0" y1="0" x2="0" y2="1"><stop offset="0" stop-color="#23304a"/><stop offset="1" stop-color="#0e121b"/></linearGradient></defs>
    <path d="M0 120 Q600 -60 1200 110 L1200 560 Q600 720 0 570 Z" fill="url(#night)"/>
    <path d="M0 120 Q600 -60 1200 110 L1200 90 Q620 -80 0 100 Z" fill="var(--green)"/>
    <path d="M0 120 Q600 -40 1200 110 Q600 -20 0 130Z" fill="#111"/>
    <path d="M0 570 Q600 720 1200 560 L1200 600 Q600 740 0 590 Z" fill="#111"/>
    <path d="M300 620 Q900 620 1200 560 L1200 580 Q900 660 300 620Z" fill="var(--green)"/>
  </svg>
  <h2>GALLERY</h2>
  <div class="shot" role="img" aria-label="Student writing at a desk" style="left:51px;top:225px;background:linear-gradient(#d8d8d4,#6a6a66)"></div>
  <div class="shot" role="img" aria-label="Teacher with young children playing" style="left:329px;top:121px;background:linear-gradient(#e8d4c0,#c2483a)"></div>
  <div class="shot" role="img" aria-label="Girls in school uniform" style="left:329px;top:335px;background:linear-gradient(#c9b8a4,#2c3a5a)"></div>
  <div class="shot" role="img" aria-label="Teacher in front of a class" style="left:617px;top:121px;background:linear-gradient(#f0f0f0,#4a68a8)"></div>
  <div class="shot" role="img" aria-label="Children using a tablet" style="left:617px;top:335px;background:linear-gradient(#c9b07a,#3a5aa8)"></div>
  <div class="shot" role="img" aria-label="Children drawing at a table" style="left:898px;top:225px;background:linear-gradient(#d9e8f2,#e3a050)"></div>
  <div class="abs dots" style="left:0;top:579px"><i class="on"></i><i></i><i></i><i></i></div>
</section>

<section class="abs contact">
  <svg class="abs" style="left:0;top:0" width="1200" height="480" viewBox="0 0 1200 480">
    <path d="M0 120 Q600 -40 1200 90 L1200 480 L0 480 Z" fill="#4a3040"/>
    <path d="M0 120 Q600 -40 1200 90 L1200 60 Q600 -70 0 100 Z" fill="#111"/>
    <path d="M400 50 Q900 0 1200 70 L1200 50 Q900 -20 400 50Z" fill="var(--green)"/>
    <path d="M600 60 Q900 40 1200 100 L1200 476 L600 476 Z" fill="#111"/>
  </svg>
  <div class="abs map" role="img" aria-label="Road map of Belgium, the Netherlands and northern France showing the school location"></div>
  <svg class="abs map-pin" width="36" height="48" viewBox="0 0 24 32"><path fill="var(--pin)" d="M12 0a11 11 0 0 0-11 11c0 9 11 21 11 21s11-12 11-21A11 11 0 0 0 12 0z"/><circle cx="12" cy="11" r="4.5" fill="#fff"/></svg>
  <h2 class="abs" style="left:600px;top:125px;width:550px;text-align:center;color:#fff;font-size:29px;font-weight:600">CONTACT US</h2>
  <div class="field" style="left:656px;top:208px;width:198px;height:41px">Name</div>
  <div class="field" style="left:895px;top:208px;width:198px;height:41px">Email</div>
  <div class="field" style="left:656px;top:280px;width:433px;height:77px;border-radius:14px">Message</div>
  <div class="submit"><svg width="18" height="18" viewBox="0 0 24 24"><path fill="#fff" d="M2 11 22 2l-6 20-4-8z"/></svg>Submit</div>
</section>

<footer class="abs footer">
  <p>© 2019 Copyrights @ Lycée Royal de Velmont All Rights Reserved</p>
  <div class="social"><span></span><span></span><span></span><span></span></div>
</footer>

</body>
</html>
```